Double-sided business card needed - specific brief

We need a double sided business card designed for our company Radiant Trimline. Having lost a lot of weight myself, the back of the card needs to show my before and after pictures. It needs to cover the entire back side of the card. This might be with my two before pictures over set on top of my main after picture or in separate frames. I'll leave that to your artistic consideration. The front needs to have our logo with contact details centred below.

The cards will be printed by PRINTKO.com and will be rectangular, 84mm x 55mm, but with ROUNDED edges. Please therefore present your designs rectangular but with rounded edges if possible.

The card should be designed in LANDSCAPE orientation.

As well as the logo, the front of the card should have the following details:

Moira Blakewell
Weight Loss Motivator with 189lb personal loss
moira@radiant-trimline.example
+44 (0)7700 900418

The website is important so should perhaps be more bold than the rest:
www.radiant-trimline.example

My brand colours are: Pink #CD2366, Light Pink #FD88AD. Blue #1C9CB1, Light Blue #64C4DE

Target Market(s)

Women 30+

Contact Information for Business Card

As description above

Font styles to use
Sans Serif

Requirements
Must have
• Double sided.
• Back side entirely covered with my before and after pictures.
• You may wish to float my before pictures on top of my after picture or add them in different frames. I look forward to seeing your different suggestions.

```html
<!DOCTYPE html>
<html lang="en">
<head>
<meta charset="utf-8">
<title>Radiant Trimline – Business Card</title>
<link href="https://fonts.googleapis.com/css2?family=Cinzel:wght@400;600&family=Questrial&display=swap" rel="stylesheet">
<style>
  :root {
    --backdrop: #8ba6ad;
    --card: #f6f6f4;
    --ink: #1a1a1a;
    --panel-dark: #231f20;
    --brand-pink: #cd2366;
    --brand-blue: #1c9cb1;
    --icon-gold: #f2c230;
    --circle-blue: #2b3a93;
    --text-grey: #444;
  }
  * { box-sizing: border-box; margin: 0; padding: 0; }
  html, body { width: 1200px; height: 800px; overflow: hidden; }
  body { background: var(--backdrop); position: relative; font-family: "Questrial", sans-serif; }

  .card {
    position: absolute;
    left: 396px;
    width: 414px;
    height: 237px;
    background: var(--card);
    overflow: hidden;
  }
  .card--front { top: 119px; }
  .card--back { top: 430px; }

  /* Front */
  .front-panel { position: absolute; inset: 0; width: 414px; height: 237px; }
  .brand {
    position: absolute;
    left: 12px; top: 24px;
    width: 190px;
    display: flex; flex-direction: column; align-items: center; gap: 8px;
  }
  .brand__mark {
    width: 56px; height: 56px; border-radius: 50%;
    background: var(--brand-pink);
  }
  .brand__name {
    font-family: "Cinzel", serif;
    font-weight: 400;
    font-size: 22px;
    line-height: 1;
    color: var(--brand-pink);
    text-align: center;
    white-space: nowrap;
  }
  .holder {
    position: absolute; left: 20px; top: 141px;
    font-family: "Cinzel", serif; font-weight: 600;
    font-size: 16px; color: var(--ink); letter-spacing: .3px;
  }
  .contacts { position: absolute; left: 14px; top: 170px; list-style: none; }
  .contacts li {
    display: flex; align-items: center; gap: 5px;
    height: 15px; font-size: 9px; color: var(--text-grey);
  }
  .contacts li.contacts__web { font-size: 11px; color: var(--ink); }
  .contacts svg { width: 12px; height: 12px; flex: none; }

  /* Back */
  .photo { position: absolute; top: 0; height: 114px; }
  .photo--before { left: 29px; width: 176px; background: linear-gradient(135deg, #c08a72, #e9dcd4 55%, #8a2a22); }
  .photo--after { left: 209px; width: 176px; background: linear-gradient(135deg, #8a6d4e, #3a2a22 50%, #2a3660); }
  .centre-circle {
    position: absolute; left: 145px; top: 114px;
    width: 124px; height: 124px; border-radius: 50%;
    background: var(--circle-blue);
  }
  .photo--middle {
    position: absolute; left: 171px; top: 128px; width: 73px; height: 97px;
    background: linear-gradient(180deg, #7e9a6a, #d8d6e0 55%, #5d8a50);
  }
  .label {
    position: absolute; display: flex; flex-direction: column; align-items: center; gap: 6px;
    font-family: "Cinzel", serif; font-weight: 600; font-size: 17px; color: var(--ink);
  }
  .label--before { left: 60px; top: 144px; }
  .label--after { left: 294px; top: 146px; }
  .label svg { width: 14px; height: 28px; }
</style>
</head>
<body>
  <section class="card card--front" aria-label="Card front">
    <svg class="front-panel" viewBox="0 0 414 237" aria-hidden="true">
      <path d="M326 0 Q348 6 345 60 Q338 170 268 237 L414 237 L414 0 Z" fill="var(--panel-dark)"/>
    </svg>
    <div class="brand">
      <span class="brand__mark" aria-hidden="true"></span>
      <span class="brand__name">Radiant Trimline</span>
    </div>
    <h1 class="holder">Moira Blakewell</h1>
    <ul class="contacts">
      <li><svg viewBox="0 0 12 12"><circle cx="6" cy="6" r="6" fill="var(--icon-gold)"/><rect x="3.5" y="3" width="5" height="6" fill="none" stroke="#333" stroke-width="1"/></svg>Weight Loss Motivator with 189lb personal loss</li>
      <li><svg viewBox="0 0 12 12"><circle cx="6" cy="6" r="6" fill="var(--icon-gold)"/><rect x="4.2" y="2.8" width="3.6" height="6.4" rx=".8" fill="#333"/></svg>+44 (0)7700 900418</li>
      <li><svg viewBox="0 0 12 12"><circle cx="6" cy="6" r="6" fill="var(--icon-gold)"/><rect x="3" y="4" width="6" height="4.2" fill="none" stroke="#333" stroke-width="1"/><path d="M3 4 L6 6.5 L9 4" fill="none" stroke="#333" stroke-width="1"/></svg>moira@radiant-trimline.example</li>
      <li class="contacts__web"><svg viewBox="0 0 12 12"><circle cx="6" cy="6" r="6" fill="var(--icon-gold)"/><circle cx="6" cy="6" r="3" fill="none" stroke="#333" stroke-width="1"/><path d="M3 6 H9 M6 3 V9" stroke="#333" stroke-width=".8"/></svg>www.radiant-trimline.example</li>
    </ul>
  </section>

  <section class="card card--back" aria-label="Card back">
    <div class="photo photo--before" role="img" aria-label="Before photo: bride in a veil and tiara"></div>
    <div class="photo photo--after" role="img" aria-label="After photo: woman seated on a leather sofa beside flowers"></div>
    <div class="centre-circle" aria-hidden="true"></div>
    <div class="photo--middle" role="img" aria-label="Before photo: woman in a garden holding a small dog"></div>
    <div class="label label--before">
      <svg viewBox="0 0 14 28" aria-hidden="true"><path d="M7 1 L13 11 H8.5 V27 H5.5 V11 H1 Z" fill="var(--ink)"/></svg>
      Before
    </div>
    <div class="label label--after">
      <svg viewBox="0 0 14 28" aria-hidden="true"><path d="M7 1 L13 11 H8.5 V27 H5.5 V11 H1 Z" fill="var(--ink)"/></svg>
      After
    </div>
  </section>
</body>
</html>
```